Professional business cards for real estate development company

I need business cards for my new real estate development company. The company, "LUMAR" is a real estate development, investment, and advisory firm with a focus on multifamily, office, and mixed-use projects across primary and secondary markets in the Southeast United States.

Style preference is modern

Industry/Entity Type

Real Estate Development

Contact Information for Business Card

The business cards need to include:
Name
Title
Mailing Address
Phone Number
Web Address

Logo is attached. I would like white to be the primary color with incorporation of the company colors: #232D3A and #B5A451

Font styles to use
Other font styles liked:
• Montserrat, Avenir

Requirements
Must have
• Company Logo. No need to include the company name since the name is in the logo.
Should not have
• No line type designs

```html
<!DOCTYPE html>
<html lang="en">
<head>
<meta charset="UTF-8">
<title>LUMAR Business Card</title>
<link href="https://fonts.googleapis.com/css2?family=Montserrat:wght@400;500;700&display=swap" rel="stylesheet">
<style>
  :root {
    --navy: #232D3A;
    --navy-soft: #2c3848;
    --gold: #B5A451;
    --white: #ffffff;
    --ink: #1a1f27;
    --rule: #c9ccd1;
    --stage: #e6e7e9;
  }
  * { box-sizing: border-box; margin: 0; padding: 0; }
  html, body {
    width: 1200px; height: 1015px; overflow: hidden;
    background: var(--stage);
    font-family: "Montserrat", sans-serif;
  }
  .sheet {
    position: relative; width: 1200px; height: 1015px;
    display: flex; flex-direction: column; align-items: center; justify-content: center; gap: 60px;
  }
  .card {
    position: relative; width: 700px; height: 400px;
    box-shadow: 0 10px 30px rgba(0,0,0,.18);
    overflow: hidden;
  }
  /* Back */
  .card-back { background: var(--navy); }
  .back-pattern {
    position: absolute; inset: 0;
    background: linear-gradient(135deg, var(--navy-soft) 0%, var(--navy) 60%);
  }
  .back-mark {
    position: absolute; right: 150px; top: 250px;
    display: flex; align-items: center; gap: 10px;
    color: var(--gold); font-weight: 500; font-size: 26px; letter-spacing: 2px;
  }
  .back-mark .square { width: 18px; height: 18px; background: var(--gold); }
  /* Front */
  .card-front { background: var(--white); display: flex; }
  .front-brand {
    width: 56%; display: flex; align-items: center; justify-content: center; gap: 18px;
  }
  .front-brand .square { width: 46px; height: 46px; background: var(--navy); }
  .front-brand .name {
    color: var(--navy); font-weight: 700; font-size: 64px; letter-spacing: 4px;
  }
  .divider {
    align-self: center; width: 1px; height: 260px; background: var(--rule);
  }
  .front-contact {
    flex: 1; padding: 0 0 0 34px; display: flex; flex-direction: column; justify-content: center;
    color: var(--ink);
  }
  .person-name { font-weight: 700; font-size: 24px; color: var(--navy); letter-spacing: .5px; }
  .person-title { font-weight: 500; font-size: 15px; margin-bottom: 16px; }
  .contact-line { display: flex; align-items: center; gap: 10px; font-size: 15px; line-height: 1.7; }
  .contact-line svg { width: 15px; height: 15px; flex: none; }
  .address { margin-top: 14px; font-size: 15px; line-height: 1.45; }
</style>
</head>
<body>
<main class="sheet">
  <section class="card card-back">
    <div class="back-pattern" role="img" aria-label="Repeating faint brand pattern in dark navy tones"></div>
    <div class="back-mark"><span class="square"></span><span>LUMAR</span></div>
  </section>

  <section class="card card-front">
    <div class="front-brand">
      <span class="square"></span>
      <span class="name">LUMAR</span>
    </div>
    <div class="divider"></div>
    <div class="front-contact">
      <p class="person-name">DANIEL REYES</p>
      <p class="person-title">Managing Director</p>
      <p class="contact-line">
        <svg viewBox="0 0 24 24"><path fill="#232D3A" d="M6.6 10.8a15 15 0 0 0 6.6 6.6l2.2-2.2a1 1 0 0 1 1-.25 11.4 11.4 0 0 0 3.6.57 1 1 0 0 1 1 1V20a1 1 0 0 1-1 1A17 17 0 0 1 3 4a1 1 0 0 1 1-1h3.5a1 1 0 0 1 1 1c0 1.25.2 2.45.57 3.57a1 1 0 0 1-.25 1z"/></svg>
        044-555 210 347
      </p>
      <p class="contact-line">
        <svg viewBox="0 0 24 24"><path fill="#232D3A" d="M2 5h20v14H2z"/><path fill="none" stroke="#fff" stroke-width="1.6" d="M2 5l10 8 10-8"/></svg>
        info@lumardev.com
      </p>
      <p class="contact-line">
        <svg viewBox="0 0 24 24" fill="none" stroke="#232D3A" stroke-width="2"><circle cx="12" cy="12" r="10"/><path d="M2 12h20M12 2c3 3 3 17 0 20M12 2c-3 3-3 17 0 20"/></svg>
        www.lumardev.com
      </p>
      <p class="address">218 Harbor Lane Suite 4<br>Savannah, GA 31401</p>
    </div>
  </section>
</main>
</body>
</html>
```